We are in search of a new business card design for our business. We have a Mexican Grocery Store called Tortilla Grove Market, we would like to see that some have mexican design, but we are open to any type of designs.

Phone: to be announced
Fax: to be announced

Address is:
2415 Calloway Blvd
Harborview, MD 21990

```html
<!DOCTYPE html>
<html lang="en">
<head>
<meta charset="UTF-8">
<title>Tortilla Grove Market – Business Card</title>
<link rel="stylesheet" href="https://fonts.googleapis.com/css2?family=Roboto:wght@400;700&display=swap">
<style>
  :root {
    --bg: #ece8e2;
    --green: #137a5a;
    --white: #ffffff;
    --red: #d0202a;
    --yellow: #f2dc1a;
    --ink: #6e2a2e;
    --shadow: rgba(0, 0, 0, 0.18);
  }
  * { box-sizing: border-box; margin: 0; padding: 0; }
  html, body {
    width: 1200px;
    height: 902px;
    overflow: hidden;
    background: var(--bg);
    font-family: "Roboto", Arial, sans-serif;
  }
  .card {
    position: absolute;
    left: 75px;
    top: 151px;
    width: 1050px;
    height: 600px;
    background: var(--white);
    box-shadow: 0 14px 36px var(--shadow);
    overflow: hidden;
  }
  .flag {
    display: flex;
    height: 480px;
  }
  .flag__stripe { flex: 1; }
  .flag__stripe--green { background: var(--green); }
  .flag__stripe--white {
    background: var(--white);
    display: flex;
    align-items: center;
    justify-content: center;
    gap: 14px;
  }
  .flag__stripe--red { background: var(--red); }
  .brand__dot {
    width: 26px;
    height: 26px;
    border-radius: 50%;
    background: var(--red);
    flex: none;
  }
  .brand__name {
    font-weight: 700;
    font-size: 30px;
    line-height: 1.1;
    color: var(--ink);
    text-align: left;
  }
  .divider {
    height: 5px;
    background: var(--yellow);
  }
  .contacts {
    height: 115px;
    display: flex;
    align-items: center;
    justify-content: space-between;
    padding: 0 60px;
    color: var(--ink);
    font-size: 24px;
    font-weight: 400;
    white-space: nowrap;
  }
  .contact {
    display: flex;
    align-items: center;
    gap: 12px;
  }
  .contact__icon {
    width: 28px;
    height: 28px;
    fill: var(--ink);
    flex: none;
  }
</style>
</head>
<body>
  <section class="card" aria-label="Tortilla Grove Market business card">
    <div class="flag">
      <div class="flag__stripe flag__stripe--green"></div>
      <div class="flag__stripe flag__stripe--white">
        <span class="brand__dot"></span>
        <span class="brand__name">Tortilla Grove<br>Market</span>
      </div>
      <div class="flag__stripe flag__stripe--red"></div>
    </div>
    <div class="divider"></div>
    <div class="contacts">
      <div class="contact contact--phone">
        <svg class="contact__icon" viewBox="0 0 24 24" aria-hidden="true">
          <path d="M6.6 10.8a15.1 15.1 0 0 0 6.6 6.6l2.2-2.2c.3-.3.7-.4 1-.2 1.1.4 2.3.6 3.6.6.6 0 1 .4 1 1V20c0 .6-.4 1-1 1A17 17 0 0 1 3 4c0-.6.4-1 1-1h3.5c.6 0 1 .4 1 1 0 1.3.2 2.5.6 3.6.1.3 0 .7-.2 1z"/>
        </svg>
        <span>555.014.2280</span>
      </div>
      <div class="contact contact--address">
        <svg class="contact__icon" viewBox="0 0 24 24" aria-hidden="true">
          <path d="M12 3 2 12h3v8h5v-5h4v5h5v-8h3z"/>
        </svg>
        <span>2415 Calloway Blvd, Harborview, MD 21990</span>
      </div>
      <div class="contact contact--fax">
        <svg class="contact__icon" viewBox="0 0 24 24" aria-hidden="true">
          <path d="M7 3h8l3 3v3H7zM3 10h18v8h-3v3H6v-3H3zm5 5v4h8v-4z"/>
        </svg>
        <span>555.014.2280</span>
      </div>
    </div>
  </section>
</body>
</html>
```